Business cards design on a high standard

We advise clients on insurance and financial matters, since these clients pay for our advice, the design should have a high standard. Our logo should be included. From the colors we are open for everything.

Colors

Designer to choose colors to be used in the design.

```html
<!DOCTYPE html>
<html lang="en">
<head>
<meta charset="utf-8">
<title>Alpine Counsel – Business Card</title>
<link href="https://fonts.googleapis.com/css2?family=Open+Sans:ital,wght@0,400;0,700;1,400;1,700&display=swap" rel="stylesheet">
<style>
  :root {
    --stage: #2b2b2d;
    --card-dark: #1d1d1f;
    --card-light: #ffffff;
    --brand-red: #e3202a;
    --text-grey: #555559;
  }
  html, body {
    margin: 0;
    width: 1200px;
    height: 900px;
    overflow: hidden;
    background: var(--stage);
    font-family: "Open Sans", sans-serif;
  }
  .sheet {
    width: 1200px;
    height: 900px;
    display: flex;
    flex-direction: column;
    align-items: center;
    justify-content: center;
    gap: 40px;
  }
  .card {
    width: 560px;
    height: 320px;
    box-sizing: border-box;
    box-shadow: 0 10px 30px rgba(0,0,0,0.45);
  }
  .card-front {
    background: var(--card-dark);
    display: flex;
    align-items: center;
    justify-content: center;
  }
  .brand-name {
    color: var(--brand-red);
    font-weight: 700;
    font-size: 46px;
    letter-spacing: 3px;
    text-transform: uppercase;
  }
  .card-back {
    background: var(--card-light);
    display: flex;
    align-items: center;
    justify-content: center;
    gap: 22px;
  }
  .identity {
    text-align: right;
  }
  .person-name {
    color: var(--brand-red);
    font-weight: 700;
    font-style: italic;
    font-size: 22px;
    text-transform: uppercase;
    letter-spacing: -0.5px;
    margin: 0;
  }
  .person-role {
    color: var(--text-grey);
    font-style: italic;
    font-size: 15px;
    margin: 0;
  }
  .divider {
    width: 2px;
    height: 110px;
    background: var(--brand-red);
  }
  .contact {
    list-style: none;
    margin: 0;
    padding: 0;
    color: var(--text-grey);
    font-style: italic;
    font-size: 15px;
    line-height: 1.4;
  }
  .contact li {
    display: flex;
    align-items: center;
    gap: 6px;
  }
  .contact .address { padding-left: 18px; }
  .contact svg { width: 12px; height: 12px; fill: var(--brand-red); flex: none; }
</style>
</head>
<body>
<main class="sheet">
  <section class="card card-front">
    <span class="brand-name">Alpine Counsel</span>
  </section>

  <section class="card card-back">
    <div class="identity">
      <p class="person-name">Daniel Hartwell</p>
      <p class="person-role">President</p>
    </div>
    <div class="divider"></div>
    <ul class="contact">
      <li class="address">1870 Harbor View Drive</li>
      <li class="address">Seacliff CA 92701</li>
      <li>
        <svg viewBox="0 0 12 12" aria-hidden="true"><path d="M2.5 0.5 L4.5 0.5 L5.2 3.2 L3.8 4.3 Q5 7 7.7 8.2 L8.8 6.8 L11.5 7.5 L11.5 9.5 Q11.5 11.5 9.5 11.5 Q0.5 11 0.5 2.5 Q0.5 0.5 2.5 0.5Z"/></svg>
        555-310-4827
      </li>
      <li>
        <svg viewBox="0 0 12 12" aria-hidden="true"><path d="M0 2 H12 V10 H0Z M0.8 2.6 L6 6.6 L11.2 2.6" stroke="#fff" stroke-width="0.9"/></svg>
        dan@alpinecounsel.com
      </li>
      <li>
        <svg viewBox="0 0 12 12" aria-hidden="true"><circle cx="6" cy="6" r="5.8"/><path d="M0.5 6 H11.5 M6 0.3 V11.7 M6 0.5 Q2.5 6 6 11.5 M6 0.5 Q9.5 6 6 11.5" stroke="#fff" stroke-width="0.8" fill="none"/></svg>
        www.alpinecounsel.com
      </li>
    </ul>
  </section>
</main>
</body>
</html>
```